WP website design for Colbury

We need a wordpress design for an established auction and real estate company based in New Jersey. The winning design will incorporate a professional color scheme with company logo in a clean layout. The design needs to consider that this will be developed on a responsive theme. Colors are those that will highlight the logo

Industry/Entity Type

Real Estate

Font styles to use
Serif
Sans Serif

Requirements
Must have
• colors will be #3E3D5D and #3C7296
navigation: 1) Home 2) Auctions 3) Real Estate Listings 4) Buyers 5) Sellers 6) About Us 7 ) Contact Us
design will use a slideshow - image is attached.
Widgets to place in the header, sidebar or footer:
1) email signup form 2) social icons (facebook, twitter, youtube, RSS) 3) Featured Properties widget 4) Featured Auctions widget 5) News & Events blog 6) Featured Videos
Nice to have
• Site will have numerous dropdown menus - so it would be nice to have a sample of what the dropdowns would look like. EG 1)▪ Our Featured Listings and 2)▪ MLS Property Search under the main "Real Estate Listings" menu item.

```html
<!DOCTYPE html>
<html lang="en">
<head>
<meta charset="utf-8">
<title>Colbury Real Estate &amp; Auction</title>
<link href="https://fonts.googleapis.com/css2?family=Arimo:wght@400;700&family=Carlito:wght@400;700&display=swap" rel="stylesheet">
<style>
:root{
  --navy:#3E3D5D;
  --blue:#3C7296;
  --blue-light:#4a86ad;
  --ink:#2b2b2b;
  --muted:#444;
  --panel:#f7f6f4;
  --border:#cfcfcf;
  --footer:#444444;
  --white:#ffffff;
}
*{box-sizing:border-box;margin:0;padding:0}
html,body{width:790px;height:1200px;overflow:hidden}
body{position:relative;background:var(--white);font-family:"Arimo",Arial,sans-serif;color:var(--ink)}
.abs{position:absolute}

/* header */
.brand{left:67px;top:40px;display:flex;align-items:center;gap:8px}
.brand-square{width:22px;height:22px;background:var(--navy)}
.brand-name{font-family:"Arimo",sans-serif;font-weight:700;font-size:26px;color:var(--navy);letter-spacing:.5px}
.social{top:31px;display:flex;gap:7px;left:561px}
.social span{width:34px;height:34px;border-radius:50%;display:block}
.social .s1{background:#1d4f7a}.social .s2{background:#2aa3dd}.social .s3{background:#ee8a12}.social .s4{background:#b8b8b8}

/* navigation */
.nav-band{left:0;top:100px;width:790px;height:60px;background:var(--navy)}
.hero-bg{left:0;top:160px;width:790px;height:328px;background:linear-gradient(#ffffff,#e9e9ea)}
.nav{left:0;top:100px;width:790px;height:38px;font-size:10.5px;color:var(--white);text-transform:uppercase}
.nav a{position:absolute;top:14px;color:var(--white);text-decoration:none}
.nav .active{top:8px;padding:6px 5px;background:var(--blue);border-radius:3px}

.dropdown{left:244px;top:136px;width:136px;height:92px;background:#e3e3e3;box-shadow:0 1px 3px rgba(0,0,0,.3)}
.dropdown::before{content:"";position:absolute;left:63px;top:-6px;border:6px solid transparent;border-top:0;border-bottom-color:#e3e3e3}
.dropdown li{list-style:none;position:absolute;left:6px;width:122px;height:19px;border-radius:2px;background:#3a3a3a;color:var(--white);font-size:8px;line-height:19px;padding-left:15px}
.dropdown li::before{content:"";position:absolute;left:7px;top:6px;border-left:4px solid #fff;border-top:3.5px solid transparent;border-bottom:3.5px solid transparent}
.dropdown li.on{background:var(--blue)}

/* slider */
.slider-frame{left:68px;top:142px;width:654px;height:300px;background:var(--white);box-shadow:0 8px 10px -6px rgba(0,0,0,.35)}
.slide{left:71px;top:144px;width:648px;height:297px;background:linear-gradient(180deg,#9dbbd8 0%,#cfd6c6 30%,#a9a98a 55%,#4f7b37 80%,#3e6b2c 100%)}
.signup{left:490px;top:197px;width:199px;height:184px;background:rgba(60,114,150,.82);color:var(--white);padding:14px 12px}
.signup h2{font-family:"Carlito",sans-serif;font-weight:400;font-size:21px;letter-spacing:.3px}
.signup p{font-family:"Carlito",sans-serif;font-size:8.5px;line-height:10.5px;margin-top:3px}
.signup .field{position:absolute;left:13px;width:161px;height:18px;background:var(--white);color:#888;font-size:8.5px;line-height:18px;padding-left:5px}
.signup .btn{position:absolute;left:13px;top:142px;width:90px;height:22px;border-radius:11px;background:var(--white);border:2px solid #2c5e80;box-shadow:0 0 0 2px #8fb8d3;color:var(--navy);font-family:"Carlito",sans-serif;font-weight:700;font-size:9.5px;text-align:center;line-height:18px}
.dots{left:362px;top:461px;display:flex;gap:5px}
.dots span{width:12px;height:12px;border-radius:50%;background:#e6e6e6;border:2px solid #bbb;box-shadow:inset 0 0 0 1.5px #fff}
.dots span.on{background:#6d6d6d}

/* welcome */
.welcome{left:68px;top:510px;width:410px}
.welcome h1{font-family:"Carlito",sans-serif;font-weight:400;font-size:19.5px;color:var(--ink);letter-spacing:.3px;margin-bottom:9px}
.welcome p{font-size:8.3px;line-height:13px;color:#333;margin-bottom:13px}
.divider{left:503px;top:512px;height:558px;border-left:1px dashed #aaa}

.video{left:520px;top:513px;width:190px;height:136px;background:#1b1b1b;box-shadow:0 10px 8px -8px rgba(0,0,0,.35)}
.video-still{left:524px;top:517px;width:182px;height:119px;background:linear-gradient(160deg,#7d8c9e,#4e5a3e 55%,#3a3b45)}
.video-bar{left:524px;top:637px;width:182px;height:9px;background:#111}

/* listing cards */
.card{left:67px;width:418px;height:181px;background:linear-gradient(#ffffff,#f1f0ee);border:1px solid var(--border)}
.card-head{position:absolute;left:3px;top:3px;width:412px;height:28px;background:var(--navy);color:var(--white);font-weight:700;font-size:11px;line-height:28px;padding-left:11px;letter-spacing:.3px}
.card-photo{position:absolute;left:14px;top:48px;width:139px;height:94px;background:linear-gradient(180deg,#6f9ccf 0%,#9fb9c9 40%,#c9c7c0 60%,#5d8a3a 85%)}
.card-body{position:absolute;left:163px;top:51px;width:245px;font-size:8.3px;color:#222}
.card-body h3{font-size:10.5px;letter-spacing:.4px;color:#333;margin-bottom:6px}
.card-body .meta{line-height:13px}
.card-body .meta.loc{font-size:9.3px}
.card-body .desc{margin-top:7px;line-height:12px;font-size:7.9px}
.card-btns{position:absolute;left:13px;top:151px;display:flex;gap:1px}
.card-btns span{height:22px;background:var(--blue);color:var(--white);font-size:8.3px;letter-spacing:.4px;display:flex;align-items:center;gap:5px;padding:0 6px;white-space:nowrap}
.card-btns svg{flex-shrink:0}
.card-btns span:first-child{width:68px}
.card-btns span:last-child{width:72px;padding-left:8px}

/* sidebar widgets */
.widget{left:522px;width:190px;height:182px;background:linear-gradient(#ffffff,#efefef);border:1px solid var(--border);padding:12px 12px}
.widget h4{font-size:11px;letter-spacing:.3px;color:#222;margin-bottom:9px}
.feat-photo{width:166px;height:78px;background:linear-gradient(180deg,#98b9de 0%,#c8d6e0 45%,#3d7c25 55%,#2f6a1b 100%)}
.feat-text{font-size:8px;color:#111;line-height:10px;margin-top:9px;padding-left:3px}
.feat-text .loc{margin-top:4px;font-size:8.5px}
.news{display:flex;gap:7px;margin-bottom:14px}
.news-thumb{flex:0 0 45px;height:33px;background:linear-gradient(135deg,#5b86b8,#c9a97b);border:1px solid #bbb}
.news-text{font-size:8.3px;line-height:12px;color:#222}
.news-text b{color:var(--navy);font-family:"Carlito",sans-serif;font-size:9.5px}
.news-text i{display:block;text-align:right;font-size:7.8px;margin-top:3px}

/* footer */
.footer{left:0;top:1094px;width:790px;height:82px;background:var(--footer)}
.footer-info{left:72px;top:1110px;color:var(--white);font-size:8.5px;line-height:14.5px}
.badges{left:455px;top:1116px;display:flex;align-items:center;gap:10px}
.badges span{display:block;background:#e8e8e8}
.copyright{left:0;top:1176px;width:790px;height:24px;background:var(--blue);border-top:2px solid #2e5c7c;color:var(--white);font-size:7.8px;text-align:center;line-height:22px}
</style>
</head>
<body>

<header>
  <div class="abs brand"><span class="brand-square"></span><span class="brand-name">COLBURY</span></div>
  <div class="abs social" aria-label="Social links">
    <span class="s1" role="img" aria-label="Social network page"></span>
    <span class="s2" role="img" aria-label="Short updates feed"></span>
    <span class="s3" role="img" aria-label="News feed"></span>
    <span class="s4" role="img" aria-label="Email"></span>
  </div>
</header>

<div class="abs nav-band"></div>
<div class="abs hero-bg"></div>

<section aria-label="Slideshow">
  <div class="abs slider-frame"></div>
  <div class="abs slide" role="img" aria-label="Photo of a suburban house with a front garden and green lawn"></div>
  <form class="abs signup">
    <h2>Email Sign Up</h2>
    <p>Lorem ipsum dolor sit amet, consectetuer adipiscing elit. Nam</p>
    <div class="field" style="top:74px">Your Name</div>
    <div class="field" style="top:107px">Email Address</div>
    <div class="btn">Subscribe Now</div>
  </form>
  <div class="abs dots"><span class="on"></span><span></span><span></span><span></span></div>
</section>

<nav class="abs nav">
  <a style="left:87px">Home</a>
  <a style="left:157px">Auctions</a>
  <a class="active" style="left:242px">Real Estate Listings</a>
  <a style="left:391px">Buyers</a>
  <a style="left:470px">Sellers</a>
  <a style="left:553px">About Us</a>
  <a style="left:642px">Contact Us</a>
</nav>
<ul class="abs dropdown">
  <li class="on" style="top:14px">Lorem Ipsum is simply</li>
  <li style="top:39px">dummy text of the printing</li>
  <li style="top:64px">Typesetting industry.</li>
</ul>

<main>
  <article class="abs welcome">
    <h1>Welcome to Colbury Real Estate &amp; Auction</h1>
    <p>Lorem Ipsum is that it has a more-or-less normal distribution of letters, as opposed to using 'Content here, content here', making it look like readable English. Many desktop publishing packages and web page editors now use Lorem Ipsum as their default model text, and a search for 'lorem ipsum' will uncover many web sites still in their infancy. Various versions have evolved over the years, some-times</p>
    <p>by accident, sometimes on purpose (injected humour and the likelike readable English. Many desktop publishing packages and web page editors now use Lorem Ipsum as their default model text, and a search for 'lorem ipsum' will uncover many web sites still in their infancy.</p>
  </article>

  <div class="abs divider"></div>

  <div class="abs video"></div>
  <div class="abs video-still" role="img" aria-label="Video still of an auctioneer speaking to an outdoor crowd"></div>
  <svg class="abs" style="left:594px;top:552px" width="36" height="36" viewBox="0 0 36 36" aria-hidden="true">
    <circle cx="18" cy="18" r="16" fill="#222" fill-opacity=".85" stroke="#fff" stroke-width="2"/>
    <path d="M14 10 L26 18 L14 26 Z" fill="#fff"/>
  </svg>
  <div class="abs video-bar"></div>
  <svg class="abs" style="left:526px;top:638px" width="178" height="7" aria-hidden="true">
    <circle cx="4" cy="3.5" r="2.5" fill="#ddd"/>
    <rect x="11" y="3" width="120" height="1" fill="#666"/>
    <rect x="140" y="1.5" width="8" height="4" fill="#888"/>
    <rect x="160" y="3" width="14" height="1" fill="#aaa"/>
  </svg>

  <section class="abs card" style="top:683px">
    <div class="card-head">FURNITURE ‘ ANTIQUES ’ COLLECTIBLES</div>
    <div class="card-photo" role="img" aria-label="Photo of a two-storey family house with garage"></div>
    <div class="card-body">
      <h3>FURNITURE ‘ ANTIQUES ’ COLLECTIBLES</h3>
      <div class="meta"><b>Begins:</b>&nbsp; Saturday, March 16, 2013 at 10:00 AM EDT</div>
      <div class="meta loc"><b>Location:</b>&nbsp; 2158 Alder Road Millbrook, NJ 07801</div>
      <div class="desc">Harlow BS3F High Lift, simply dummy text of the printing and typesetting industry simply dummy text of the printing and type-setting industry 600 Series Tarrant tractor w/Brennick Loader, Dune buggy, 1207.</div>
    </div>
    <div class="card-btns">
      <span><svg width="14" height="8" aria-hidden="true"><rect width="4" height="8" fill="#fff"/><rect x="6" y="0" width="8" height="1.6" fill="#fff"/><rect x="6" y="3.2" width="8" height="1.6" fill="#fff"/><rect x="6" y="6.4" width="8" height="1.6" fill="#fff"/></svg>DETAILS</span>
      <span><svg width="14" height="11" aria-hidden="true"><rect x=".5" y=".5" width="13" height="10" fill="none" stroke="#fff"/><path d="M2 9 L6 4 L9 7 L10.5 5.5 L12.5 9Z" fill="#fff"/></svg>GALLERY</span>
    </div>
  </section>

  <section class="abs card" style="top:888px">
    <div class="card-head">FURNITURE ‘ ANTIQUES ’ COLLECTIBLES</div>
    <div class="card-photo" role="img" aria-label="Photo of a two-storey family house with garage"></div>
    <div class="card-body">
      <h3>FURNITURE ‘ ANTIQUES ’ COLLECTIBLES</h3>
      <div class="meta"><b>Begins:</b>&nbsp; Saturday, March 16, 2013 at 10:00 AM EDT</div>
      <div class="meta loc"><b>Location:</b>&nbsp; 2158 Alder Road Millbrook, NJ 07801</div>
      <div class="desc">Harlow BS3F High Lift, simply dummy text of the printing and typesetting industry simply dummy text of the printing and type-setting industry 600 Series Tarrant tractor w/Brennick Loader, Dune buggy, 1207.</div>
    </div>
    <div class="card-btns">
      <span><svg width="14" height="8" aria-hidden="true"><rect width="4" height="8" fill="#fff"/><rect x="6" y="0" width="8" height="1.6" fill="#fff"/><rect x="6" y="3.2" width="8" height="1.6" fill="#fff"/><rect x="6" y="6.4" width="8" height="1.6" fill="#fff"/></svg>DETAILS</span>
      <span><svg width="14" height="11" aria-hidden="true"><rect x=".5" y=".5" width="13" height="10" fill="none" stroke="#fff"/><path d="M2 9 L6 4 L9 7 L10.5 5.5 L12.5 9Z" fill="#fff"/></svg>GALLERY</span>
    </div>
  </section>

  <aside>
    <section class="abs widget" style="top:684px">
      <h4>FEATURED AUCTION</h4>
      <div class="feat-photo" role="img" aria-label="Photo of farmland with a green field and silos"></div>
      <div class="feat-text">
        <div><b>Begins:</b>&nbsp; Saturday, March 16, 2013<br>at 10:00 AM EDT</div>
        <div class="loc"><b>Location:</b>&nbsp; 2158 Alder Road<br>Millbrook, NJ 07801</div>
      </div>
    </section>

    <section class="abs widget" style="top:889px">
      <h4 style="margin-bottom:12px">FEATURED AUCTION</h4>
      <div class="news">
        <div class="news-thumb" role="img" aria-label="Thumbnail of a house with a sold sign"></div>
        <div class="news-text"><b>Lorem ipsum dolor sit,</b><br>consectetur adipisicing elit,do eiusmod tempor labore et .<i>January 13, 2013</i></div>
      </div>
      <div class="news">
        <div class="news-thumb" role="img" aria-label="Thumbnail of a house with a sold sign"></div>
        <div class="news-text"><b>Lorem ipsum dolor sit,</b><br>consectetur adipisicing elit,do eiusmod tempor labore et .<i>January 13, 2013</i></div>
      </div>
    </section>
  </aside>
</main>

<footer>
  <div class="abs footer"></div>
  <address class="abs footer-info" style="font-style:normal">
    Colbury Real Estate &amp; Auction Inc.<br>
    480 Harwood Ave., Trenton NJ 08608<br>
    office@colburyauc.com &nbsp;&nbsp;Phone: (609) 555 0148
  </address>
  <div class="abs badges" aria-label="Member associations">
    <span role="img" aria-label="Association badge" style="width:30px;height:34px"></span>
    <span role="img" aria-label="Association badge" style="width:88px;height:28px"></span>
    <span role="img" aria-label="Association badge" style="width:76px;height:28px"></span>
    <span role="img" aria-label="Association badge" style="width:30px;height:28px;border-radius:50%"></span>
  </div>
  <div class="abs copyright">Copyright (c) Colbury Auctions, Inc. 2014. All Right Reserved</div>
</footer>

</body>
</html>
```